Lotus Leaf Kitchen Road Billboard

Road Billboard I need all of this information on it
Authentic Thai Food Bangkok Style
6.5 Miles on the right
4126 Maple Ridge Rd Otto NC
828-555-4172

```html
<!DOCTYPE html>
<html lang="en">
<head>
<meta charset="utf-8">
<title>Lotus Leaf Kitchen Road Billboard</title>
<link rel="stylesheet" href="https://fonts.googleapis.com/css2?family=Montserrat:wght@700;800&display=swap">
<style>
  :root {
    --paper: #ffffff;
    --board: #050505;
    --gold: #d4a82a;
    --white: #ffffff;
    --red: #e4292a;
    --ink: #0a0a0a;
    --chevron-grey: #cfcfcf;
  }
  html, body {
    margin: 0;
    padding: 0;
    width: 1200px;
    height: 529px;
    overflow: hidden;
    background: var(--paper);
  }
  .billboard {
    position: absolute;
    left: 96px;
    top: 118px;
    width: 1010px;
    height: 295px;
    background: var(--board);
    overflow: hidden;
    font-family: "Montserrat", sans-serif;
  }
  .hero-photo {
    position: absolute;
    left: 440px;
    top: 0;
    width: 570px;
    height: 295px;
    background:
      radial-gradient(ellipse 90px 150px at 150px 150px, rgba(245,140,30,0.85), rgba(200,60,10,0.35) 60%, transparent 100%),
      radial-gradient(ellipse 120px 150px at 310px 130px, rgba(150,70,40,0.7), rgba(40,70,30,0.5) 55%, transparent 100%),
      radial-gradient(ellipse 120px 60px at 480px 140px, rgba(120,120,120,0.45), transparent 100%),
      linear-gradient(90deg, var(--board) 0%, #140804 30%, #120a06 70%, var(--board) 100%);
  }
  .headline {
    position: absolute;
    left: 64px;
    top: 26px;
    margin: 0;
    color: var(--gold);
    font-weight: 800;
    font-size: 60px;
    line-height: 56px;
    letter-spacing: -2.5px;
    text-transform: uppercase;
  }
  .headline span { display: block; }
  .tagline {
    position: absolute;
    left: 64px;
    top: 134px;
    margin: 0;
    color: var(--white);
    font-weight: 700;
    font-size: 46px;
    line-height: 50px;
    letter-spacing: -0.5px;
  }
  .brand {
    position: absolute;
    left: 843px;
    top: 26px;
    width: 140px;
    text-align: center;
  }
  .brand-dot {
    display: block;
    width: 44px;
    height: 44px;
    margin: 0 auto 18px;
    border-radius: 50%;
    background: var(--gold);
  }
  .brand-name {
    color: var(--gold);
    font-weight: 700;
    font-size: 13px;
    white-space: nowrap;
  }
  .info-bands {
    position: absolute;
    left: 0;
    top: 0;
  }
  .phone, .directions {
    position: absolute;
    top: 215px;
    height: 52px;
    line-height: 52px;
    font-weight: 800;
    white-space: nowrap;
    text-align: center;
  }
  .phone {
    left: 90px;
    width: 280px;
    color: var(--ink);
    font-size: 36px;
    letter-spacing: -0.5px;
  }
  .directions {
    left: 400px;
    width: 418px;
    color: var(--white);
    font-size: 35px;
    letter-spacing: -1px;
  }
  .address {
    position: absolute;
    left: 868px;
    top: 209px;
    margin: 0;
    color: var(--white);
    font-style: normal;
    font-weight: 800;
    font-size: 15px;
    line-height: 21px;
    letter-spacing: -0.3px;
    white-space: nowrap;
  }
  .address span { display: block; }
</style>
</head>
<body>
  <section class="billboard">
    <div class="hero-photo" role="img" aria-label="Photo of shrimp, broccoli and vegetables tossed over a flaming wok"></div>

    <h1 class="headline"><span>Authentic</span><span>Thai Food</span></h1>
    <p class="tagline">Bangkok Style</p>

    <div class="brand">
      <span class="brand-dot"></span>
      <span class="brand-name">Lotus Leaf Kitchen</span>
    </div>

    <svg class="info-bands" width="1010" height="295" viewBox="0 0 1010 295" aria-hidden="true">
      <polygon class="band-phone" points="66,215 380,215 392,241 380,267 86,267 76,241" fill="var(--white)"/>
      <polygon class="band-directions" points="380,215 820,215 833,241 820,267 380,267 392,241" fill="var(--red)"/>
      <polygon class="chevron" points="827,218 841,218 851,241 841,264 827,264 837,241" fill="var(--chevron-grey)"/>
    </svg>

    <div class="phone">828-555-4172</div>
    <div class="directions">6.5 MILES ON THE RIGHT</div>

    <address class="address">
      <span>4126</span>
      <span>Maple Ridge Rd</span>
      <span>Otto NC</span>
    </address>
  </section>
</body>
</html>
```